Fire Hydrant Repair Parts Flyer

We need a flyer advertising both fire hydrant parts and the manufacturers that we are stocking. Our company is Coastal Flowline Supply and we are a parts distributor who sells directly to contractors. I have attached an example flyer that advertises some other parts we stock. We don't want it to look exactly like the old flyer, but we would like it to be structured similarly. I have also attached a background image for the flyer as well as some pictures of the parts we are stocking. I have also attached pictures of the manufacturer logos that we are stocking. We are trying to convey the parts that we are stocking which are: "Traffic Repair Kits", "Main Valve Repair Kits", "Extension Kits", "Replacement Caps & Gaskets", "Replacement Nozzles", Adjustable Hydrant Wrenches", "Hydrant Diffusers", & "Hydrant Oil". I have attached pictures of some of these items that we would like placed on the flyer. Let me know if you have any questions at all.

```html
<!DOCTYPE html>
<html lang="en">
<head>
<meta charset="utf-8">
<title>Fire Hydrant Parts Flyer – Coastal Flowline Supply</title>
<link href="https://fonts.googleapis.com/css2?family=Roboto+Condensed:wght@400;700&family=Roboto:wght@400;500&display=swap" rel="stylesheet">
<style>
  :root {
    --blue: #3a55a7;
    --red: #e81d4f;
    --red-dark: #c2123f;
    --grey: #efefef;
    --tile-border: #dcdcdc;
    --white: #ffffff;
    --ink: #222222;
  }
  * { margin: 0; padding: 0; box-sizing: border-box; }
  html, body { width: 848px; height: 1200px; overflow: hidden; background: var(--grey); }
  .flyer {
    position: relative; width: 848px; height: 1200px; overflow: hidden;
    background: var(--grey);
    font-family: "Roboto Condensed", "Arial Narrow", sans-serif;
  }
  .backdrop { position: absolute; inset: 0; }
  .hero-photo-label { position: absolute; left: 0; top: 0; width: 848px; height: 560px; }

  .brand {
    position: absolute; top: 30px; left: 468px;
    display: flex; align-items: center; gap: 12px;
  }
  .brand-mark { width: 34px; height: 34px; border-radius: 50%; background: var(--red); }
  .brand-name {
    font-family: "Roboto", sans-serif; font-weight: 500;
    font-size: 27px; color: var(--blue); letter-spacing: 0.2px;
  }

  .headline {
    position: absolute; right: 40px; top: 214px; text-align: right;
    font-weight: 700; line-height: 0.88; text-transform: uppercase;
  }
  .headline .main { color: var(--blue); font-size: 68px; display: block; }
  .headline .sub { color: var(--red); font-size: 40px; display: block; margin-top: 10px; }

  .contact {
    position: absolute; right: 26px; top: 538px; text-align: right; color: var(--white);
  }
  .contact .cta { font-weight: 700; font-size: 36px; line-height: 1.1; }
  .contact .phone {
    display: flex; align-items: center; justify-content: flex-end; gap: 8px;
    font-weight: 700; font-size: 52px; line-height: 1.05;
  }
  .contact .phone svg { width: 42px; height: 42px; }
  .contact .web { font-weight: 400; font-size: 30px; line-height: 1.2; }

  .parts-list {
    position: absolute; left: 23px; top: 523px; width: 376px; list-style: none;
  }
  .parts-list li {
    display: flex; align-items: center; gap: 14px;
    height: 50.5px; color: var(--white); white-space: nowrap;
    font-weight: 700; font-size: 27px; letter-spacing: -0.1px;
    border-bottom: 1.5px dashed rgba(255,255,255,0.55);
  }
  .parts-list li:last-child { border-bottom: none; }
  .parts-list li svg { width: 18px; height: 18px; flex: none; margin-left: 3px; }

  .product-grid {
    position: absolute; left: 462px; top: 740px;
    display: grid; grid-template-columns: 171px 171px; grid-auto-rows: 135px;
    column-gap: 13px; row-gap: 12px;
  }
  .product-tile {
    background: var(--white); border: 1.5px solid var(--tile-border);
    border-radius: 14px; padding: 12px; display: flex;
  }
  .product-image { flex: 1; border-radius: 8px; }
  .img-cap { background: radial-gradient(circle at 50% 40%, #d62a2a 0 22%, #c9cbd0 23% 40%, #f4f4f4 60%); }
  .img-diffuser { background: radial-gradient(circle at 50% 45%, #f2b705 0 28%, #6d6d6d 30% 36%, #f4f4f4 60%); }
  .img-oil { background: radial-gradient(ellipse 22% 45% at 50% 50%, #e9e9ea 0 80%, #f7f7f7 100%); }
  .img-kit { background: radial-gradient(ellipse at 50% 50%, #2e2f33 0 30%, #9ea3a9 40%, #f4f4f4 65%); }
  .img-extension { background: radial-gradient(ellipse at 45% 50%, #2b2c30 0 28%, #a7abb1 40%, #f4f4f4 65%); }
  .img-wrench { background: linear-gradient(135deg, #f6f6f6 30%, #b5bac0 50%, #f6f6f6 70%); }

  .maker-table {
    position: absolute; left: 26px; top: 1038px; width: 415px; height: 132px;
    display: grid; grid-template-columns: repeat(3, 1fr); grid-template-rows: repeat(2, 1fr);
    background: var(--white); border: 1px solid #cfcfcf;
  }
  .maker {
    display: flex; align-items: center; justify-content: center; gap: 6px;
    border-right: 1px solid #d8d8d8; border-bottom: 1px solid #d8d8d8;
    font-weight: 700; font-size: 15px; color: var(--ink); text-align: center; line-height: 1.05;
    padding: 4px;
  }
  .maker:nth-child(3n) { border-right: none; }
  .maker:nth-child(n+4) { border-bottom: none; }
  .maker .dot { width: 16px; height: 16px; border-radius: 50%; background: var(--red); flex: none; }
  .maker .sq { width: 16px; height: 16px; background: var(--blue); flex: none; }
</style>
</head>
<body>
<div class="flyer">
  <svg class="backdrop" width="848" height="1200" viewBox="0 0 848 1200" aria-hidden="true">
    <defs>
      <linearGradient id="heroTone" x1="0" y1="0" x2="1" y2="1">
        <stop offset="0" stop-color="#6e9a4a"/>
        <stop offset="0.22" stop-color="#8b8f93"/>
        <stop offset="0.45" stop-color="#c4c8cc"/>
        <stop offset="0.7" stop-color="#eef0f1"/>
        <stop offset="1" stop-color="#f7f7f7"/>
      </linearGradient>
      <radialGradient id="hydrantTone" cx="0.18" cy="0.5" r="0.3">
        <stop offset="0" stop-color="#c8202a"/>
        <stop offset="1" stop-color="#c8202a" stop-opacity="0"/>
      </radialGradient>
      <filter id="ringShadow" x="-20%" y="-20%" width="140%" height="140%">
        <feDropShadow dx="4" dy="6" stdDeviation="8" flood-color="#000" flood-opacity="0.18"/>
      </filter>
    </defs>
    <rect width="848" height="1200" fill="var(--grey)"/>
    <path d="M0,0 H848 V420 C720,505 560,548 390,552 C250,520 120,480 0,440 Z" fill="url(#heroTone)"/>
    <path d="M0,0 H848 V420 C720,505 560,548 390,552 C250,520 120,480 0,440 Z" fill="url(#hydrantTone)"/>
    <path d="M0,410 C40,430 70,450 95,472 L0,470 Z" fill="var(--red)"/>
    <path d="M385,552 C560,548 720,505 848,420 V692 C760,722 600,724 445,700 Z" fill="var(--red)"/>
    <path d="M445,690 C600,714 760,712 848,682 V692 C760,722 600,724 445,700 Z" fill="var(--red-dark)"/>
    <path d="M330,0 H848 V100 H470 C410,98 355,52 330,0 Z" fill="var(--white)"/>
    <path d="M330,0 C355,52 410,98 470,100" fill="none" stroke="var(--red)" stroke-width="6"/>
    <circle cx="174" cy="721" r="288" fill="var(--white)" filter="url(#ringShadow)"/>
    <circle cx="174" cy="721" r="258" fill="var(--blue)"/>
  </svg>

  <div class="hero-photo-label" role="img" aria-label="Photo of a red and silver fire hydrant on a lawn spraying a strong stream of water"></div>

  <div class="brand">
    <span class="brand-mark"></span>
    <span class="brand-name">Coastal Flowline Supply</span>
  </div>

  <h1 class="headline">
    <span class="main">Fire Hydrant</span>
    <span class="main">Parts and</span>
    <span class="sub">The Manufacturers</span>
  </h1>

  <div class="contact">
    <div class="cta">Call us Today!</div>
    <div class="phone">
      <svg viewBox="0 0 42 42" aria-hidden="true">
        <circle cx="21" cy="21" r="20" fill="#fff"/>
        <path d="M14 11c1-1 2.5-1 3.3 0l2.4 3c.7.9.6 2.1-.2 2.9l-1.4 1.3c1 2.3 2.8 4.2 5.1 5.2l1.4-1.4c.8-.8 2-.9 2.9-.2l3 2.4c1 .8 1 2.3 0 3.3l-1.7 1.7c-1.3 1.3-3.3 1.6-5 .8-5-2.4-9-6.4-11.4-11.4-.8-1.7-.5-3.7.8-5z" fill="var(--red)"/>
      </svg>
      <span>(800) 555-0148</span>
    </div>
    <div class="web">www.coastalflowline.com</div>
  </div>

  <ul class="parts-list">
    <li><svg viewBox="0 0 18 18" aria-hidden="true"><circle cx="9" cy="9" r="9" fill="#fff"/><path d="M7 5l6 4-6 4z" fill="var(--blue)"/></svg>Traffic Repair Kits</li>
    <li><svg viewBox="0 0 18 18" aria-hidden="true"><circle cx="9" cy="9" r="9" fill="#fff"/><path d="M7 5l6 4-6 4z" fill="var(--blue)"/></svg>Main Valve Repair Kits</li>
    <li><svg viewBox="0 0 18 18" aria-hidden="true"><circle cx="9" cy="9" r="9" fill="#fff"/><path d="M7 5l6 4-6 4z" fill="var(--blue)"/></svg>Extension Kits</li>
    <li><svg viewBox="0 0 18 18" aria-hidden="true"><circle cx="9" cy="9" r="9" fill="#fff"/><path d="M7 5l6 4-6 4z" fill="var(--blue)"/></svg>Replacement Caps &amp; Gaskets</li>
    <li><svg viewBox="0 0 18 18" aria-hidden="true"><circle cx="9" cy="9" r="9" fill="#fff"/><path d="M7 5l6 4-6 4z" fill="var(--blue)"/></svg>Replacement Nozzles</li>
    <li><svg viewBox="0 0 18 18" aria-hidden="true"><circle cx="9" cy="9" r="9" fill="#fff"/><path d="M7 5l6 4-6 4z" fill="var(--blue)"/></svg>Adjustable Hydrant Wrenches</li>
    <li><svg viewBox="0 0 18 18" aria-hidden="true"><circle cx="9" cy="9" r="9" fill="#fff"/><path d="M7 5l6 4-6 4z" fill="var(--blue)"/></svg>Hydrant Diffusers</li>
    <li><svg viewBox="0 0 18 18" aria-hidden="true"><circle cx="9" cy="9" r="9" fill="#fff"/><path d="M7 5l6 4-6 4z" fill="var(--blue)"/></svg>Hydrant Oil</li>
  </ul>

  <div class="product-grid">
    <div class="product-tile"><div class="product-image img-cap" role="img" aria-label="Red hydrant nozzle cap with chain"></div></div>
    <div class="product-tile"><div class="product-image img-diffuser" role="img" aria-label="Yellow hydrant diffuser with pressure gauge"></div></div>
    <div class="product-tile"><div class="product-image img-oil" role="img" aria-label="Bottle of hydrant oil"></div></div>
    <div class="product-tile"><div class="product-image img-kit" role="img" aria-label="Traffic repair kit with breakaway flange and bolts"></div></div>
    <div class="product-tile"><div class="product-image img-extension" role="img" aria-label="Hydrant extension kit with barrel section, gaskets and bolts"></div></div>
    <div class="product-tile"><div class="product-image img-wrench" role="img" aria-label="Adjustable hydrant wrench"></div></div>
  </div>

  <div class="maker-table">
    <div class="maker"><span class="sq"></span>Ridgeline Pipe</div>
    <div class="maker"><span class="dot"></span>Harlow Valve</div>
    <div class="maker">Brant Valve Co.</div>
    <div class="maker"><span class="sq"></span>Tessel</div>
    <div class="maker"><span class="dot"></span>Summit Flow Control</div>
    <div class="maker"><span class="dot"></span>Keel Valve Company</div>
  </div>
</div>
</body>
</html>
```